Stationary Design Letterhead and Envelope

Artist should provide Letterhead and envelop stationary designs

Info for stationary:
Fernhallow Outdoor Advertising
4873 Quarry Rd. 915 N. PO BOX 528617
Austin, TX 78519

Dale Fernhallow
President
555-862-1907
dale@fernhallowsigns.example
fernhallowsigns.example

Target Market(s)

clients

Colors
0054AA
0677BA
7BADD7
CADEEF
E8F1F8

Requirements
Must have
• high quality unique eye catching and dynamic

```html
<!DOCTYPE html>
<html lang="en">
<head>
<meta charset="utf-8">
<title>Fernhallow Outdoor Advertising – Stationery</title>
<link href="https://fonts.googleapis.com/css2?family=Arimo:wght@400;700&family=Questrial&display=swap" rel="stylesheet">
<style>
  :root {
    --brand-blue: #0770a9;
    --ink: #111111;
    --text: #4a4a4a;
    --paper: #ffffff;
    --backdrop: #e4e4e4;
    --rule: #3a3a3a;
  }
  * { box-sizing: border-box; margin: 0; padding: 0; }
  html, body { width: 1200px; height: 1164px; overflow: hidden; }
  body { background: var(--backdrop); font-family: "Arimo", Arial, sans-serif; color: var(--text); position: relative; }

  .sheet { position: absolute; background: var(--paper); overflow: hidden; }
  .letterhead { left: 38px; top: 199px; width: 541px; height: 766px; }
  .envelope { left: 618px; width: 543px; height: 237px; }
  .envelope--blue-flap { top: 199px; }
  .envelope--white-flap { top: 455px; }
  .envelope--front { top: 729px; }

  .wordmark { display: inline-flex; flex-direction: column; align-items: center; color: var(--ink); font-family: "Arimo", Arial, sans-serif; font-weight: 700; line-height: 1; }
  .wordmark__name { font-size: 19px; letter-spacing: 0.5px; text-transform: uppercase; }
  .wordmark__tag { font-size: 7px; letter-spacing: 0.3px; text-transform: uppercase; margin-top: 3px; }
  .wordmark--light { color: var(--paper); }

  .letterhead .wordmark { position: absolute; left: 48px; top: 40px; }

  .letterhead__address { position: absolute; right: 187px; top: 40px; text-align: right; font-size: 8.6px; line-height: 10.8px; font-style: normal; }
  .letterhead__divider { position: absolute; left: 363px; top: 39px; width: 1px; height: 31px; background: var(--rule); }
  .letterhead__contacts { position: absolute; left: 372px; top: 40px; list-style: none; font-size: 8.6px; line-height: 10.8px; }
  .letterhead__contacts li { display: flex; align-items: center; gap: 5px; }
  .letterhead__contacts svg { width: 6px; height: 6px; fill: var(--brand-blue); }

  .letter { position: absolute; left: 48px; top: 236px; width: 446px; }
  .letter__salutation { font-family: "Questrial", Arial, sans-serif; font-weight: 700; font-size: 12.5px; color: #505050; margin-bottom: 24px; }
  .letter__body p { font-size: 9.3px; line-height: 11.1px; margin-bottom: 10px; }
  .letter__closing { font-family: "Questrial", Arial, sans-serif; font-weight: 700; font-size: 7px; margin-top: 18px; }
  .letter__signature { width: 90px; height: 28px; margin-top: 16px; background: linear-gradient(90deg, #d8d8d8, #efefef); border-radius: 3px; }

  .footer-band { position: absolute; left: 0; bottom: 0; width: 100%; height: 18px; background: var(--brand-blue); }
  .footer-rule { position: absolute; left: 0; bottom: 23px; width: 100%; height: 3px; background: var(--ink); }

  .flap { position: absolute; left: 0; top: 0; width: 543px; height: 66px; display: block; }
  .envelope .flap-mark { position: absolute; top: 19px; left: 0; width: 100%; text-align: center; }

  .envelope__return { position: absolute; left: 18px; top: 17px; text-align: center; }
  .envelope__return address { font-style: normal; font-size: 7.6px; line-height: 9.4px; margin-top: 6px; color: #333; }
</style>
</head>
<body>

<section class="sheet letterhead" aria-label="Letterhead">
  <div class="wordmark">
    <span class="wordmark__name">Fernhallow</span>
    <span class="wordmark__tag">Outdoor Advertising</span>
  </div>

  <address class="letterhead__address">
    4873 Quarry Rd.<br>
    915 N. PO BOX 528617<br>
    Austin, TX 78519
  </address>
  <div class="letterhead__divider"></div>
  <ul class="letterhead__contacts">
    <li><svg viewBox="0 0 10 10"><path d="M2 0l2 2-1 2a6 6 0 003 3l2-1 2 2-2 2C4 10 0 6 0 2z"/></svg>555-862-1907</li>
    <li><svg viewBox="0 0 10 10"><path d="M0 2h10v6H0z M0 2l5 4 5-4" stroke="#fff" stroke-width=".8"/></svg>dale@fernhallowsigns.example</li>
    <li><svg viewBox="0 0 10 10"><circle cx="5" cy="5" r="5"/></svg>fernhallowsigns.example</li>
  </ul>

  <article class="letter">
    <p class="letter__salutation">Dear Mr. Carver,</p>
    <div class="letter__body">
      <p>Lorem ipsum dolor sit amet, consectetuer adipiscing elit, sed diam nonmmy nibh euismod tincidunt ut laor eet dolore magna aliquam erat volutpat. Ut wisi enim ad minim veniam, quis nostrud exerci tationmcorper suscipit lobortis nisl ut aliquip ex ea commodo consequat. Duis autem vel eum iriure dolor in hendrerit in vulputate velit esse molestie consequat, vel illum dolore eu feugiat</p>
      <p>Rorem ipsum dolor sit amet, consectetuer adipiscing elit, sed diam nonmmy nibh euismod tincidunt ut laor eet dolore magna aliquam erat volutpat. Ut wisi enim ad minim veniam, quis nostrud exerci tationmcorper suscipit lobortis nisl ut aliquip ex ea commodo consequat. Duis autem vel eum iriure dolor in hendrerit in vulputate velit esse molest</p>
      <p>Dorem ipsum dolor sit amet, consectetuer adipiscing elit, sed diam nonmmy nibh euismod tincidunt ut laor eet dolore magna aliquam erat volutpat. Ut wisi enim ad minim veniam, quis nostrud exerci tationmcorper suscipit lobortis nisl ut aliquip ex ea commodo consequat. Duis autem vel eum iriure dolor in hendrerit in suscipit lobortis nisl ut aliquip ex ea commodo consequat. Duis autem vel eum iriure dolor in hendrerit in vulputate velit esse molestie consequat, vel illum</p>
      <p>Sorem ipsum dolor sit amet, consectetuer adipiscing elit, sed diam nonmmy nibh euismod tincidunt ut laor eet dolore magna aliquam erat volutpat. Ut wisi enim ad minim veniam, quis nostrud exerci tationmcorper suscipit lobortis nisl ut aliquip ex ea commodo consequat. Duis autem vel eum iriure dolor in</p>
    </div>
    <p class="letter__closing">Sincerely,</p>
    <div class="letter__signature" role="img" aria-label="Handwritten signature"></div>
  </article>

  <div class="footer-rule"></div>
  <div class="footer-band"></div>
</section>

<section class="sheet envelope envelope--blue-flap" aria-label="Envelope back, blue flap">
  <svg class="flap" viewBox="0 0 543 66" aria-hidden="true">
    <path d="M0 0 H543 L532 44 Q526 66 504 66 H39 Q17 66 11 44z" fill="var(--brand-blue)"/>
  </svg>
  <div class="flap-mark">
    <div class="wordmark wordmark--light">
      <span class="wordmark__name">Fernhallow</span>
      <span class="wordmark__tag">Outdoor Advertising</span>
    </div>
  </div>
</section>

<section class="sheet envelope envelope--white-flap" aria-label="Envelope back, white flap">
  <svg class="flap" viewBox="0 0 543 66" aria-hidden="true">
    <path d="M0 0 H543 L532 44 Q526 66 504 66 H39 Q17 66 11 44z" fill="#ffffff" stroke="#d4d4d4" stroke-width="1"/>
  </svg>
  <div class="flap-mark">
    <div class="wordmark">
      <span class="wordmark__name">Fernhallow</span>
      <span class="wordmark__tag">Outdoor Advertising</span>
    </div>
  </div>
</section>

<section class="sheet envelope envelope--front" aria-label="Envelope front">
  <div class="envelope__return">
    <div class="wordmark">
      <span class="wordmark__name">Fernhallow</span>
      <span class="wordmark__tag">Outdoor Advertising</span>
    </div>
    <address>4873 Quarry Rd. 915 N.<br>PO BOX 528617, Austin, TX 78519</address>
  </div>
  <div class="footer-rule"></div>
  <div class="footer-band"></div>
</section>

</body>
</html>
```